Design a Brazilian children's Bible calendar for 2017

We need someone to design a children's calendar for 2017 with an animal theme.
The format is 21cm x 15cm and we need the front cover and one page with two months as can be seen in the attached files.
Target Market(s)
Brazilian children
Font styles to use
Sans Serif
Requirements
Must have
- Modern, clean design

```html
<!DOCTYPE html>
<html lang="pt-BR">
<head>
<meta charset="utf-8">
<title>Calendário Infantil 2017 — Janeiro e Fevereiro</title>
<link href="https://fonts.googleapis.com/css2?family=Open+Sans:wght@400;600&family=Arimo:wght@400;700&display=swap" rel="stylesheet">
<style>
  :root {
    --pink-bg: #f6c9d2;
    --pink-deep: #f2b9c5;
    --pink-light: #fbe3e8;
    --verse-green: #9bcc3c;
    --verse-text: #c0161d;
    --note-yellow: #fff1a6;
    --note-shadow: #e5d27a;
    --band-green: #9fd13f;
    --red: #d01a1f;
    --ink: #111;
    --cell-shade: #ececec;
    --white: #ffffff;
  }
  * { box-sizing: border-box; margin: 0; padding: 0; }
  html, body { width: 857px; height: 1200px; overflow: hidden; }
  body { font-family: "Arimo", Arial, sans-serif; background: var(--white); }

  .calendar-page { position: relative; width: 857px; height: 1200px; overflow: hidden; }

  .pattern-backdrop {
    position: absolute; left: 0; top: 0; width: 857px; height: 1160px;
    background: linear-gradient(180deg, var(--pink-bg) 0%, var(--pink-deep) 100%);
  }

  .hero-photo {
    position: absolute; left: 0; top: 0; width: 857px; height: 645px;
    background: linear-gradient(180deg, #a4ab6e 0%, #8d9850 35%, #c9a56c 60%, #b38b55 78%, #6f8a37 100%);
  }

  .verse-box {
    position: absolute; left: 145px; top: 640px; width: 565px; height: 110px;
    background: var(--verse-green); border-radius: 0 0 14px 14px;
    text-align: center; color: var(--verse-text);
    font-family: "Open Sans", Verdana, sans-serif; font-size: 36px; line-height: 36px;
    padding-top: 2px;
  }
  .verse-ref { position: absolute; right: 24px; bottom: 10px; font-size: 19px; line-height: 1; }

  .month-card { position: absolute; top: 776px; width: 390px; height: 352px; }
  .month-card.jan { left: 36px; }
  .month-card.feb { left: 442px; }
  .note {
    position: absolute; inset: 16px 4px 0 4px; background: var(--note-yellow);
    box-shadow: 3px 4px 0 var(--note-shadow);
  }
  .month-band {
    position: absolute; left: 0; right: 0; top: 0; height: 48px;
    background: var(--band-green); clip-path: polygon(0 12%, 100% 0, 100% 100%, 0 100%);
    display: flex; justify-content: space-between; align-items: flex-end;
    padding: 0 60px 6px 44px; color: var(--red); font-weight: 700; font-size: 34px;
  }
  .month-grid {
    position: absolute; left: 10px; top: 62px; width: 352px;
    display: grid; grid-template-columns: repeat(7, 1fr);
    border: 2px solid var(--red); background: var(--white);
  }
  .month-grid span {
    height: 49px; border: 1px solid var(--red); display: flex;
    align-items: center; justify-content: center; font-size: 28px; color: var(--ink);
  }
  .month-grid .day-name { height: 34px; font-weight: 700; font-size: 20px; background: var(--white); }
  .month-grid .sat, .month-grid .empty { background: var(--cell-shade); }

  .bottom-trim { position: absolute; left: 0; bottom: 0; width: 857px; height: 40px; background: var(--pink-light); }
  .bottom-trim-line { position: absolute; left: 0; top: 0; width: 857px; height: 10px; background: var(--red); }
</style>
</head>
<body>
<main class="calendar-page">
  <div class="pattern-backdrop" role="img" aria-label="Fundo xadrez rosa e branco"></div>
  <div class="hero-photo" role="img" aria-label="Fotografia de uma guepardo com dois filhotes deitados na grama"></div>

  <section class="verse-box">
    <p>No principio, criou<br>Deus os ceus<br>e a terra.</p>
    <span class="verse-ref">Genesis 1 v 1</span>
  </section>

  <section class="month-card jan">
    <div class="note"></div>
    <header class="month-band"><span>Janeiro</span><span>2017</span></header>
    <div class="month-grid">
      <span class="day-name">Dom</span><span class="day-name">Seg</span><span class="day-name">Ter</span><span class="day-name">Qua</span><span class="day-name">Qui</span><span class="day-name">Sex</span><span class="day-name">Sáb</span>
      <span>1</span><span>2</span><span>3</span><span>4</span><span>5</span><span>6</span><span class="sat">7</span>
      <span>8</span><span>9</span><span>10</span><span>11</span><span>12</span><span>13</span><span class="sat">14</span>
      <span>15</span><span>16</span><span>17</span><span>18</span><span>19</span><span>20</span><span class="sat">21</span>
      <span>22</span><span>23</span><span>24</span><span>25</span><span>26</span><span>27</span><span class="sat">28</span>
      <span>29</span><span>30</span><span>31</span><span></span><span></span><span></span><span class="empty"></span>
    </div>
  </section>

  <section class="month-card feb">
    <div class="note"></div>
    <header class="month-band"><span>Fevereiro</span><span>2017</span></header>
    <div class="month-grid">
      <span class="day-name">Dom</span><span class="day-name">Seg</span><span class="day-name">Ter</span><span class="day-name">Qua</span><span class="day-name">Qui</span><span class="day-name">Sex</span><span class="day-name">Sáb</span>
      <span></span><span></span><span></span><span>1</span><span>2</span><span>3</span><span class="sat">4</span>
      <span>5</span><span>6</span><span>7</span><span>8</span><span>9</span><span>10</span><span class="sat">11</span>
      <span>12</span><span>13</span><span>14</span><span>15</span><span>16</span><span>17</span><span class="sat">18</span>
      <span>19</span><span>20</span><span>21</span><span>22</span><span>23</span><span>24</span><span class="sat">25</span>
      <span>26</span><span>27</span><span>28</span><span></span><span></span><span></span><span class="empty"></span>
    </div>
  </section>

  <footer class="bottom-trim"><div class="bottom-trim-line"></div></footer>
</main>
</body>
</html>
```